Design a styled business card for an intimacy and attachment psychologist

I am a Psychologist providing online therapy to patients across the United States. My work is interpersonal and emotion-focused, with an emphasis on the client-therapist relationship. My primary areas of work are very personal, including sexuality and gender, abuse and trauma, and grief and loss. My target audience will be adults of all ages 18+.
My business card should convey a warm and inviting feeling of professionalism that is also casual and comfortable.
The front should be fairly simple and professional, consisting of:
- My name, Dr. Rosalind Pembrook
- My title, Licensed Psycholigist
- My logo
On either the front or the back, my contact information should be listed:
- ros@drrospembrook.example
- 555.014.7789
- drrospembrook.example
On the rear, I would like a description of the areas that I specialize in. This can be formatted in any way that appears stylistically interesting.
Individual and Couples
Relationships and Infidelity
Sexual Health & Aging
Gender Identity & Sexual Orientation
Abuse and Trauma
Sexual Compulsivity & Addiction
Sexual Dysfunction
Target Market(s)
My target audience will be adults of all ages 18+.
Industry/Entity Type
Psychology
Contact Information for Business Card
The front should be fairly simple and professional, consisting of: - My name, Dr. Rosalind Pembrook - My title, Licensed Psycholigist - My logo On either the front or the back, my contact information should be listed: - ros@drrospembrook.example - 555.014.7789 - drrospembrook.example On the rear, I would like a description of the areas that I specialize in. This can be formatted in any way that appears stylistically interesting. Individual and Couples Relationships and Infidelity Sexual Health & Aging Gender Identity & Sexual Orientation Abuse and Trauma Sexual Compulsivity & Addiction Sexual Dysfunction

```html
<!DOCTYPE html>
<html lang="en">
<head>
<meta charset="utf-8">
<title>Dr. Rosalind Pembrook – Business Card</title>
<link href="https://fonts.googleapis.com/css2?family=Cinzel:wght@500&family=Raleway:wght@400;500&display=swap" rel="stylesheet">
<style>
  :root {
    --page-bg: #d3d4d6;
    --card-dark: #2c2650;
    --card-light: #ffffff;
    --ink: #241d4b;
    --ink-soft: #2e2e34;
    --on-dark: #ffffff;
    --teal: #6cc4b0;
    --purple: #8e4fa0;
    --coral: #e2393d;
  }
  * { box-sizing: border-box; margin: 0; padding: 0; }
  html, body { width: 900px; height: 1200px; overflow: hidden; }
  body { background: var(--page-bg); position: relative; font-family: "Raleway", sans-serif; }

  .card { position: absolute; left: 188px; width: 525px; height: 298px; border-radius: 10px; overflow: hidden; }
  .card-back { top: 275px; background: var(--card-dark); color: var(--on-dark); }
  .card-front { top: 605px; background: var(--card-light); color: var(--ink); }

  .brand-dot { position: absolute; border-radius: 50%; background: var(--teal); border: 3px solid var(--on-dark); }
  .card-back .brand-dot { left: 83px; top: 69px; width: 82px; height: 82px; }
  .card-front .brand-dot { left: 27px; top: 25px; width: 68px; height: 68px; border-color: var(--ink); }

  .brand-name { position: absolute; font-family: "Cinzel", serif; font-weight: 500; line-height: 1; }
  .card-back .brand-name { left: 30px; top: 164px; width: 190px; text-align: center; font-size: 25px; color: var(--on-dark); }
  .card-front .brand-name { left: 109px; top: 25px; font-size: 21px; color: var(--ink); }
  .brand-name span { display: block; margin-bottom: 3px; }

  .specialties { position: absolute; left: 245px; top: 36px; list-style: none; }
  .specialties li { display: flex; align-items: center; height: 29px; font-size: 13px; letter-spacing: 0.1px; }
  .specialties li::before { content: ""; width: 12px; height: 12px; border: 1.3px solid var(--on-dark); border-radius: 50%; margin-right: 6px; flex: none; }

  .person-name { position: absolute; left: 28px; top: 162px; font-family: "Cinzel", serif; font-weight: 500; font-size: 22px; letter-spacing: 0.6px; color: var(--ink); }
  .person-title { position: absolute; left: 27px; top: 191px; font-size: 12.5px; color: var(--ink-soft); }

  .contact { position: absolute; left: 27px; top: 214px; list-style: none; }
  .contact li { display: flex; align-items: center; height: 20px; font-size: 12.5px; color: var(--ink-soft); letter-spacing: 0.3px; }
  .contact li.phone { letter-spacing: 2px; }
  .contact svg { width: 13px; height: 13px; margin-right: 6px; flex: none; }
</style>
</head>
<body>

<section class="card card-back" aria-label="Card back: areas of specialty">
  <div class="brand-dot" aria-hidden="true"></div>
  <div class="brand-name"><span>Dr.</span><span>Rosalind</span><span>Pembrook</span></div>
  <ul class="specialties">
    <li>Stylistically Interesting.</li>
    <li>Individual and Couples</li>
    <li>Relationships and Infidelity</li>
    <li>Sexual Health &amp; Aging</li>
    <li>Gender Identity &amp; Sexual Orientation</li>
    <li>Abuse and Trauma</li>
    <li>Sexual Compulsivity &amp; Addiction</li>
    <li>Sexual Dysfunction</li>
  </ul>
</section>

<section class="card card-front" aria-label="Card front: name and contact">
  <div class="brand-dot" aria-hidden="true"></div>
  <div class="brand-name"><span>Dr.</span><span>Rosalind</span><span>Pembrook</span></div>

  <h1 class="person-name">Dr. Rosalind Pembrook</h1>
  <p class="person-title">Licensed Psycholigist</p>

  <ul class="contact">
    <li class="phone">
      <svg viewBox="0 0 16 16" aria-hidden="true"><path fill="#e2393d" d="M3.2 1.5l2.4-.4 1.3 3.3-1.6 1.2c.8 1.8 2.1 3.2 3.9 4l1.2-1.6 3.3 1.3-.4 2.4c-.2.9-1 1.4-1.9 1.3C6.2 12.4 2.6 8.8 1.9 3.4c-.1-.9.4-1.7 1.3-1.9z"/></svg>
      555.014.7789
    </li>
    <li>
      <svg viewBox="0 0 16 16" aria-hidden="true"><rect x="1" y="3" width="14" height="10" fill="#6cc4b0"/><path d="M1 3.5l7 5 7-5" fill="none" stroke="#fff" stroke-width="1.2"/></svg>
      ros@drrospembrook.example
    </li>
    <li>
      <svg viewBox="0 0 16 16" aria-hidden="true"><circle cx="8" cy="8" r="7" fill="#8e4fa0"/><path d="M1 8h14M8 1c2.5 2.5 2.5 11.5 0 14M8 1c-2.5 2.5-2.5 11.5 0 14" fill="none" stroke="#fff" stroke-width=".9"/></svg>
      www.drrospembrook.example
    </li>
  </ul>
</section>

</body>
</html>
```